Home Page Design

Please see design brief attached. Concept here: mockboard[dot]net/file/qr83TpLM5wnePxHbUoKVsY/Velvetcourse---Landing-Page?node-id=0%3A1&t=KPwq7ZnRb2xTcVuM-1

Industry/Entity Type

Wedding

Number of Pages Required

1 page

Font styles to use
Serif
Sans Serif
Decorative
Script

Colors
A7469A
B969AE
D3A5CF
EDDBEB
F8F0F9
6B429C
8869AF
B7A5CE
E3DAEB
F3F0F8

Requirements
Must have
• Please see attached PDF
Nice to have
• Please see attached PDF
Should not have
• Please see attached PDF

```html
<!DOCTYPE html>
<html lang="en">
<head>
<meta charset="utf-8">
<title>Velvetcourse — Home</title>
<link rel="stylesheet" href="https://fonts.googleapis.com/css2?family=Playfair+Display:ital,wght@0,400;1,400&family=Jost:ital,wght@0,300;0,400;1,300&family=Cormorant+Garamond:ital,wght@1,500&display=swap">
<style>
  :root {
    --plum: #6B429C;
    --lilac-wash: #EDDBEB;
    --ink: #2c2c2c;
    --muted: #7b7b7b;
    --rule: #6B429C;
    --white: #ffffff;
    --chat: #a9a9a9;
  }
  * { margin: 0; padding: 0; box-sizing: border-box; }
  html, body { width: 902px; height: 1200px; overflow: hidden; background: var(--white); }
  .page { position: relative; width: 902px; height: 1200px; font-family: "Jost", sans-serif; color: var(--ink); }
  .abs { position: absolute; }

  /* Header */
  .brand { left: 51px; top: 5px; font-family: "Playfair Display", serif; font-size: 11px; color: var(--plum); display: flex; align-items: center; gap: 5px; }
  .brand-dot { width: 8px; height: 8px; border-radius: 50%; background: var(--plum); }
  .nav { top: 9px; left: 622px; font-size: 8px; font-weight: 400; }
  .nav a { color: var(--ink); text-decoration: none; position: absolute; white-space: nowrap; }
  .nav a.active { color: var(--plum); }
  .account { left: 866px; top: 8px; display: flex; align-items: center; gap: 6px; }
  .avatar { width: 10px; height: 10px; border-radius: 50%; background: #8a7a70; }

  /* Hero */
  .hero { left: 10px; top: 31px; width: 873px; height: 317px; background: radial-gradient(ellipse at 40% 35%, #b39a7c 0%, #7d5e44 45%, #3e2b1e 100%); }
  .hero-name { left: 0; width: 902px; top: 186px; text-align: center; font-family: "Playfair Display", serif; font-size: 30px; color: var(--white); letter-spacing: 1px; }
  .hero-rule { left: 538px; top: 233px; width: 73px; height: 1px; background: rgba(255,255,255,.8); }
  .chat { left: 872px; top: 352px; width: 29px; height: 29px; background: var(--chat); display: flex; align-items: center; justify-content: center; }

  /* Feature blocks */
  .wash { background: var(--lilac-wash); }
  .photo { overflow: hidden; }
  .title { font-family: "Playfair Display", serif; color: var(--plum); white-space: nowrap; }
  .title .cap { font-size: 40px; line-height: 1; font-style: italic; }
  .title .rest { font-style: italic; font-size: 11px; letter-spacing: 2.5px; margin-left: 1px; }
  .copy { font-size: 6.6px; font-weight: 300; line-height: 11.6px; color: var(--muted); letter-spacing: .4px; }
  .link { font-family: "Cormorant Garamond", serif; font-style: italic; font-weight: 500; font-size: 8.2px; color: var(--ink); display: flex; align-items: center; gap: 7px; white-space: nowrap; }
  .link .line { width: 32px; height: 1px; background: var(--rule); }
  .author { font-style: italic; font-weight: 300; font-size: 6.6px; color: var(--muted); }

  /* Footer */
  .footer-text { font-family: "Cormorant Garamond", serif; font-style: italic; font-weight: 500; font-size: 8.2px; line-height: 12px; color: var(--ink); white-space: nowrap; }
  .footer-text u { text-decoration: underline; }
  .divider { width: 1px; height: 26px; background: var(--plum); top: 1140px; }
  .cta { left: 571px; top: 1143px; width: 93px; height: 25px; background: var(--plum); color: var(--white); font-family: "Cormorant Garamond", serif; font-style: italic; font-weight: 500; font-size: 8px; display: flex; align-items: center; justify-content: center; }
</style>
</head>
<body>
<div class="page">

  <header>
    <div class="abs brand"><span class="brand-dot"></span>Velvetcourse</div>
    <nav class="abs nav">
      <a class="active" style="left:0">Home</a>
      <a style="left:34px">About</a>
      <a style="left:68px">Services</a>
      <a style="left:107px">Testimonials</a>
      <a style="left:160px">Gallery</a>
      <a style="left:196px">Contact</a>
    </nav>
    <div class="abs account">
      <span class="avatar"></span>
      <svg width="7" height="5" viewBox="0 0 7 5"><path d="M.5 .8 3.5 4 6.5 .8" fill="none" stroke="#6B429C" stroke-width=".8"/></svg>
    </div>
  </header>

  <section>
    <div class="abs hero" role="img" aria-label="Rustic wedding reception table with flowers, candles and place settings"></div>
    <div class="abs hero-name">Velvetcourse</div>
    <div class="abs hero-rule"></div>
    <div class="abs chat">
      <svg width="13" height="12" viewBox="0 0 13 12"><path d="M6.5 1C3.2 1 1 2.9 1 5.2c0 1.3.7 2.4 1.8 3.1L2.4 11l2.8-1.8c.4.1.9.1 1.3.1 3.3 0 5.5-1.9 5.5-4.1S9.8 1 6.5 1z" fill="#fff"/><path d="M4 4.5h5M4 6.3h4" stroke="#a9a9a9" stroke-width=".9"/></svg>
    </div>
  </section>

  <section class="feature-services">
    <div class="abs wash" style="left:470px;top:389px;width:262px;height:188px"></div>
    <div class="abs photo" style="left:430px;top:425px;width:253px;height:180px;background:linear-gradient(120deg,#3a3b32 0%,#8a6a4e 45%,#c99b74 70%,#6e6a5e 100%)" role="img" aria-label="Bride's hair being styled with a ribbon"></div>
    <svg class="abs" style="left:441px;top:505px" width="10" height="18" viewBox="0 0 10 18"><path d="M9 1 1 9l8 8" fill="none" stroke="#fff" stroke-width="1"/></svg>
    <svg class="abs" style="left:663px;top:511px" width="5" height="8" viewBox="0 0 5 8"><path d="M1 1l3 3-3 3" fill="none" stroke="#fff" stroke-width=".7"/></svg>
    <div class="abs title" style="left:223px;top:426px"><span class="cap">S</span><span class="rest">ervices</span></div>
    <p class="abs copy" style="left:225px;top:482px;width:156px">I'm a paragraph. Click here to add your own text and edit me. It's easy. Just click “Edit Text” or double click me to add your own content and make changes to the font. I'm a great place for you to tell a story and let your users know a little more about you.</p>
    <div class="abs link" style="left:225px;top:564px">View Our Packages<span class="line"></span></div>
  </section>

  <section class="feature-gallery">
    <div class="abs wash" style="left:159px;top:635px;width:262px;height:188px"></div>
    <div class="abs photo" style="left:209px;top:670px;width:253px;height:181px;background:linear-gradient(100deg,#5a4636 0%,#8c6a4c 30%,#b8b1a4 45%,#5a5550 70%,#3b3733 100%)" role="img" aria-label="Jar of baby's breath tied to a wooden chapel pew"></div>
    <div class="abs title" style="left:532px;top:667px"><span class="cap">G</span><span class="rest">allery</span></div>
    <p class="abs copy" style="left:527px;top:729px;width:134px;line-height:10.7px">I'm a paragraph. Click here to add your own text and edit me. It's easy. Just click “Edit Text” or double click me to add your own content and make changes to the font.</p>
    <div class="abs link" style="left:527px;top:822px">View Photos<span class="line"></span></div>
  </section>

  <section class="feature-testimonials">
    <div class="abs wash" style="left:472px;top:868px;width:261px;height:188px"></div>
    <div class="abs photo" style="left:433px;top:905px;width:253px;height:180px;background:linear-gradient(110deg,#efe0c4 0%,#e2c6a2 40%,#b08a6a 65%,#5c4638 100%)" role="img" aria-label="Groom kissing the bride's forehead in warm light"></div>
    <div class="abs title" style="left:227px;top:903px"><span class="cap">T</span><span class="rest">estimonials</span></div>
    <p class="abs copy" style="left:225px;top:963px;width:124px;line-height:10.6px">“I would recommend Lumen Vows to anyone looking to have a beautiful and happy wedding”</p>
    <div class="abs author" style="left:225px;top:1007px">- Nora Ellis</div>
    <div class="abs link" style="left:225px;top:1031px">More Testimonials<span class="line"></span></div>
  </section>

  <footer>
    <div class="abs footer-text" style="left:230px;top:1142px">214 Maple Arbor Lane<br>Portland, OR 97205</div>
    <div class="abs divider" style="left:328px"></div>
    <div class="abs footer-text" style="left:342px;top:1142px">Tel: 555-010-2846<br>Email: info@vcourse.com</div>
    <div class="abs divider" style="left:432px"></div>
    <div class="abs footer-text" style="left:443px;top:1143px">© 2035 by Lumen Vows.<br>Powered and secured by <u>Sitecraft</u></div>
    <div class="abs cta">Book a Consultation</div>
  </footer>

</div>
</body>
</html>
```